Tolvane Air Center needs a new upscale business card design for our high end aircraft hangar complex

Tolvane Air Center (TAC) is a large, upscale jet hangar complex in the US housing expensive aircraft. We need a new business card design, using our current logo. We will be attending a industry convention and need a card design that will stand out and be remembered by aircraft owners and private pilots.

Target Market(s)

Aircraft pilots or owners looking for a new upscale hangar

Industry/Entity Type

Airport

I like to use very heavy card stock, 400#, double sided. Square, no rounded edges please.

Colors
3276b5
0255a3
85abd2

Requirements
Must have
• An expensive, classy design, vivid colors.
Nice to have
• Needs to look very expensive and classy, and have some "pop". Designer must be able to download or copy my current typeface or fonts.
• One card side might be black with the "Logo and Tolvane Air Center Double line image in blue (or try gold, or glossy black), and perhaps have a grayed out "R470 jet silhouette". The other card side would have our contact info, and perhaps the "TAC Logo only". I'd like my contact info 'stacked', not in a paragraph format.
Should not have
• Should not look "too busy". Having a double-sided card will help.

```html
<!DOCTYPE html>
<html lang="en">
<head>
<meta charset="utf-8">
<title>Tolvane Air Center – Business Card</title>
<link rel="stylesheet" href="https://fonts.googleapis.com/css2?family=Russo+One&family=Arimo:wght@400;700&display=swap">
<style>
  :root {
    --page-bg: #e9eaec;
    --card-black: #0b0b0d;
    --card-black-soft: #26272b;
    --panel-navy: #1c1f2a;
    --swoosh-blue: #2a6790;
    --swoosh-blue-light: #3276b5;
    --brand-blue: #0255a3;
    --ink: #1a1a1f;
    --paper: #ffffff;
    --silver: #d9dadd;
    --shade: #b9bcc2;
  }
  * { margin: 0; padding: 0; box-sizing: border-box; }
  html, body { width: 1200px; height: 1020px; overflow: hidden; }
  body {
    background: var(--page-bg);
    font-family: "Arimo", Arial, sans-serif;
    display: flex;
    flex-direction: column;
    align-items: center;
    justify-content: space-evenly;
  }
  .card {
    position: relative;
    width: 820px;
    height: 456px;
    overflow: hidden;
    box-shadow: 0 6px 18px rgba(0,0,0,.22);
  }

  /* Front side */
  .card-front {
    background:
      linear-gradient(180deg, rgba(255,255,255,.06) 0%, rgba(255,255,255,.02) 28%, rgba(0,0,0,0) 29%),
      radial-gradient(ellipse at 50% 45%, var(--card-black-soft) 0%, var(--card-black) 70%);
    display: flex;
    align-items: center;
    justify-content: center;
  }
  .brand-lockup {
    text-align: center;
    font-family: "Russo One", sans-serif;
    color: var(--silver);
    font-weight: 400;
    line-height: 1;
  }
  .brand-initials { font-size: 118px; letter-spacing: 6px; }
  .brand-name { font-size: 36px; letter-spacing: 3px; margin-top: 14px; text-transform: uppercase; }

  /* Back side */
  .card-back { background: var(--paper); }
  .card-back .backdrop { position: absolute; inset: 0; width: 100%; height: 100%; }
  .back-mark {
    position: absolute;
    left: 50px; top: 40px;
    font-family: "Russo One", sans-serif;
    font-size: 26px;
    letter-spacing: 2px;
    color: var(--silver);
  }
  .holder {
    position: absolute;
    left: 266px; top: 40px;
  }
  .holder-name {
    font-family: "Russo One", sans-serif;
    font-size: 34px;
    letter-spacing: 1.5px;
    color: var(--ink);
    text-transform: uppercase;
    line-height: 1;
  }
  .holder-name .surname { color: var(--brand-blue); }
  .holder-title { font-size: 25px; color: var(--ink); margin-top: 8px; }
  .contact-list {
    position: absolute;
    left: 266px; top: 180px;
    list-style: none;
  }
  .contact-item {
    display: flex;
    align-items: center;
    height: 34px;
    margin-bottom: 18.5px;
    font-size: 27px;
    color: var(--ink);
  }
  .contact-key {
    width: 31px; height: 31px;
    background: var(--brand-blue);
    color: var(--paper);
    font-weight: 700;
    font-size: 26px;
    display: flex; align-items: center; justify-content: center;
    margin-right: 12px;
  }
  .divider-shade {
    position: absolute;
    left: 674px; top: 150px;
    width: 6px; height: 240px;
    background: linear-gradient(90deg, rgba(0,0,0,0), rgba(0,0,0,.18), rgba(0,0,0,0));
    -webkit-mask: linear-gradient(180deg, transparent, #000 30%, #000 70%, transparent);
            mask: linear-gradient(180deg, transparent, #000 30%, #000 70%, transparent);
  }
</style>
</head>
<body>

  <section class="card card-front" aria-label="Card front">
    <div class="brand-lockup">
      <div class="brand-initials">TAC</div>
      <div class="brand-name">Tolvane Air Center</div>
    </div>
  </section>

  <section class="card card-back" aria-label="Card back">
    <svg class="backdrop" viewBox="0 0 531 295" preserveAspectRatio="none" aria-hidden="true">
      <defs>
        <linearGradient id="swoosh" x1="0" y1="0" x2="1" y2="1">
          <stop offset="0" stop-color="#3276b5"/>
          <stop offset="1" stop-color="#245c82"/>
        </linearGradient>
        <linearGradient id="shade" x1="0" y1="0" x2="1" y2="0">
          <stop offset="0" stop-color="#9ea2a8"/>
          <stop offset="1" stop-color="#ffffff"/>
        </linearGradient>
      </defs>
      <rect width="531" height="295" fill="#1c1f2a"/>
      <path d="M150 0 C70 110 25 190 0 245 L0 295 L205 295 C140 205 128 100 168 0 Z" fill="url(#swoosh)"/>
      <path d="M168 0 C128 100 140 205 205 295 L531 295 L531 0 Z" fill="url(#shade)"/>
      <path d="M180 0 C142 100 154 205 222 295 L531 295 L531 0 Z" fill="#ffffff"/>
    </svg>

    <div class="back-mark">TAC</div>

    <div class="holder">
      <div class="holder-name">Wesley R. <span class="surname">Halden</span></div>
      <div class="holder-title">Logistic director</div>
    </div>

    <ul class="contact-list">
      <li class="contact-item"><span class="contact-key">P</span>+123.123.456.789</li>
      <li class="contact-item"><span class="contact-key">M</span>wesley.halden@tac.com</li>
      <li class="contact-item"><span class="contact-key">W</span>tolvaneaircenter.com</li>
      <li class="contact-item"><span class="contact-key">A</span>123 Street, State, ST 12345</li>
    </ul>

    <div class="divider-shade" aria-hidden="true"></div>
  </section>

</body>
</html>
```